Psychotherapy and emotion coaching with vaLumo requires web design

I need a web design for emotion coaching (release of emotional blockages) (psychotherapy) with the target group trauma-related disorders and anxiety disorders. The website should be clear and well-organized, i.e. rather simple. The colors should be light, blue, green and yellow are desirable. The design should radiate security.

A logo already exists and should be used appropriately.

Three columns should describe the following
-Emotion regulation
-Imaginative structure constellations
-Ego-State-Therapy

An outdated draft can be seen here:
www.ruhiger-morgen.de
The website should advertise coded in Wordpress.

I need the landing page, for which there are drafts now, and at least one more page (maybe a template) for further information (like "About me")

Target Market(s)

Clients for coaching and therapy with trauma or axienty disorders;

Coding

Coded - Design and coding required

Number of Pages Required

3 page

Font styles to use
Sans Serif

Colors
0054AA
0677BA
7BADD7
CADEEF
E8F1F8
59FF00
82FF00
B8FF75
E3FFCB
F4FFEA
FFF300
FFF600
FEFA6F
FFFEC7
FFFEE8

Requirements
Nice to have
• Title: "More happiness and satisfaction in life"
Should not have
• "Therapy" should not be listed in the header; Instead "More happiness and satisfaction in life"

```html
<!DOCTYPE html>
<html lang="en">
<head>
<meta charset="utf-8">
<title>Stille Wege – More Happiness and Satisfaction in Life</title>
<link rel="stylesheet" href="https://fonts.googleapis.com/css2?family=Open+Sans:wght@400;600;700&family=Ubuntu:wght@400;500;700&display=swap">
<style>
:root{
  --green:#5ec72e;
  --green-bright:#6fd634;
  --orange:#f6a320;
  --navy:#1c3a53;
  --navy-deep:#16304a;
  --ink:#2f3f55;
  --text:#5d6877;
  --muted:#8a93a0;
  --sky:#eef7fc;
  --line:#d9e2ea;
  --white:#ffffff;
  --blue:#2f7de1;
}
*{box-sizing:border-box;margin:0;padding:0}
html,body{width:1200px;height:4320px;overflow:hidden}
body{position:relative;font-family:"Open Sans",Arial,sans-serif;color:var(--text);background:var(--white)}
.abs{position:absolute}
.head-font{font-family:"Ubuntu","Open Sans",sans-serif}

/* header */
.topbar{left:0;top:0;width:1200px;height:80px;background:var(--white)}
.topstrip{left:0;top:0;width:1200px;height:32px}
.topstrip-info{top:8px;font-size:10px;color:#e8edf2;left:468px;display:flex;gap:46px;align-items:center}
.quote-btn{left:845px;top:10px;width:110px;height:14px;background:#3b8a99;color:#e8f4f6;font-size:9px;text-align:center;line-height:14px;letter-spacing:.3px}
.brand{left:68px;top:26px;display:flex;align-items:center;gap:14px}
.brand-dot{width:34px;height:34px;border-radius:50%;background:var(--orange)}
.brand-name{font-size:15px;line-height:17px;color:#6b7380}
.nav{top:50px;left:404px;display:flex;gap:0;font-size:11px;font-weight:600;color:#555f6b}
.nav span{margin-right:40px}
.nav .active{color:var(--navy)}

/* hero */
.hero-photo{left:0;top:80px;width:1200px;height:710px;background:linear-gradient(90deg,#0b0c0e 0%,#2b2a2a 22%,#7d746d 45%,#a8a29c 70%,#c3c0bc 100%)}
.hero-title{left:129px;top:262px;font-size:44px;line-height:50px;font-weight:700;color:var(--white)}
.hero-text{left:129px;top:386px;width:460px;font-size:20px;line-height:28px;color:#f0f0f0}
.btn-orange{background:var(--orange);color:var(--white);font-weight:700;border-radius:22px;text-align:center}
.hero-btn{left:129px;top:503px;width:154px;height:39px;line-height:39px;font-size:12px;letter-spacing:.4px}

/* about */
.sky{background:var(--sky)}
.about{left:0;top:788px;width:1200px;height:614px}
.eyebrow{font-size:13px;color:var(--orange);display:inline-block;border-bottom:1.5px solid var(--orange);padding-bottom:3px}
.center{left:0;width:1200px;text-align:center}
.section-title{font-size:44px;font-weight:700;color:var(--green)}
.about-text{left:175px;width:850px;top:976px;font-size:13.5px;line-height:22px;text-align:center;color:#5f6a78}
.card{top:1084px;width:275px;height:241px;background:var(--white);box-shadow:0 6px 18px rgba(40,70,100,.1);border-bottom:4px solid var(--green);text-align:center}
.card-title{font-size:22px;font-weight:500;color:#4a5568;letter-spacing:.5px}
.card-icon{position:absolute;left:112px;top:62px}
.card .card-title.low{position:absolute;left:0;width:100%;top:150px}
.card-pro-title{position:absolute;left:0;width:100%;top:36px}
.card-pro-text{position:absolute;left:38px;width:200px;top:88px;font-size:13.5px;line-height:21px;color:#5f6a78}

/* minds */
.minds-eyebrow{left:134px;top:1530px;font-size:11px}
.minds-title{left:134px;top:1563px;font-size:38px;line-height:46px;font-weight:700;color:var(--green)}
.minds-sub{left:134px;top:1680px;font-size:20px;font-weight:500;color:var(--ink)}
.minds-text{left:134px;width:460px;font-size:12.5px;line-height:19px;color:#6c7684}
.btn-contact{left:134px;top:1852px;width:134px;height:39px;background:var(--orange);color:var(--white);font-size:14px;font-weight:600;display:flex;align-items:center;justify-content:center;gap:12px}
.circle{border-radius:50%}

/* services */
.services{left:0;top:2058px;width:1200px;height:452px}
.svc-vertical{background:var(--navy)}
.vlabel{position:absolute;transform:rotate(-90deg);transform-origin:left top;white-space:nowrap;color:var(--white)}
.vlabel b{font-size:17px;font-weight:700;display:block}
.vlabel small{font-size:13px;color:#d9e2ea}
.svc-overlay{left:399px;top:2250px;width:401px;height:260px;background:linear-gradient(180deg,rgba(28,58,83,0) 0%,rgba(28,58,83,.85) 45%,rgba(28,58,83,.95) 100%)}
.svc-title{left:439px;top:2381px;font-size:16px;font-weight:700;color:var(--white)}
.svc-text{left:439px;top:2405px;width:330px;font-size:13px;line-height:20px;color:#eef2f6}

/* testimonials */
.testi{left:0;top:2509px;width:1200px;height:646px}
.testi-label{top:2574px;font-size:17px;color:var(--orange)}
.testi-title{top:2603px;font-size:33px;font-weight:500;color:var(--green)}
.testi-text{left:290px;width:620px;top:2895px;font-size:18px;line-height:32px;text-align:center;color:#3e4a5a}
.stars{top:3004px;font-size:20px;color:var(--orange);letter-spacing:2px}
.testi-name{top:3034px;font-size:18px;font-weight:600;color:var(--orange)}
.testi-role{top:3064px;font-size:11px;color:#333}
.arrow-btn{width:46px;height:46px;border-radius:50%;display:flex;align-items:center;justify-content:center}

/* contact */
.contact-title{left:139px;top:3278px;font-size:37px;line-height:44px;color:var(--green)}
.contact-title b{font-weight:500}
.contact-text{left:139px;top:3390px;width:380px;font-size:13.5px;line-height:22px;color:#6c7684}
.contact-rule{left:139px;top:3484px;width:381px;height:1px;background:var(--line)}
.contact-row{left:139px;display:flex;align-items:center;gap:22px;font-size:13.5px;color:#6c7684}
.contact-ico{width:38px;height:38px;border-radius:50%;background:#fff3e0;display:flex;align-items:center;justify-content:center}
.form-card{left:588px;top:3218px;width:487px;height:546px;background:var(--white);border-top:3px solid var(--navy);box-shadow:0 6px 22px rgba(40,70,100,.12);border-radius:6px}
.f-label{font-size:14px;font-weight:700;color:#3a6a8f}
.f-input{border:1px solid #c7ced6;height:42px;font-size:12px;color:#97a0aa;padding:13px 16px}
.submit{left:618px;top:3667px;width:126px;height:40px;line-height:40px;background:var(--orange);color:var(--white);font-size:13px;font-weight:700;text-align:center;letter-spacing:.5px}

/* footer */
.footer-h{font-size:15px;font-weight:700;color:var(--white);letter-spacing:.3px}
.footer-small{font-size:12px;line-height:21px;color:#e3e9ef}
.footer-brand{left:502px;top:4010px;font-size:30px;line-height:34px;color:#eef2f6;text-align:center;width:340px}
.social{width:36px;height:36px;border:1px solid #c8d3dd}
.hours{right:94px;text-align:right;font-size:12px;color:#e3e9ef;display:flex;align-items:center;gap:16px}
</style>
</head>
<body>

<!-- HEADER -->
<div class="abs topbar"></div>
<svg class="abs topstrip" width="1200" height="32" viewBox="0 0 1200 32">
  <path d="M400 0 H1200 V32 H452 C440 32 436 6 400 0 Z" fill="#4d4f53"/>
</svg>
<div class="abs topstrip-info">
  <span>● 8 Lindenhof, Musterstadt 10115</span>
  <span>Follow Us: &nbsp;▪ ▪ ▪</span>
</div>
<div class="abs quote-btn">GET QUOTATION</div>
<div class="abs brand">
  <div class="brand-dot"></div>
  <div class="brand-name">Stille Wege<br>&nbsp;&nbsp;&nbsp;&nbsp;&nbsp;&nbsp;&nbsp;&nbsp;...zur Gelassenheit</div>
</div>
<nav class="abs nav">
  <span class="active">Home</span><span>Services</span><span>About Us</span><span>Our Team</span><span>And more</span><span>Contact Us</span>
</nav>

<!-- HERO -->
<div class="abs hero-photo" role="img" aria-label="Photo of a smiling family of three sitting together on a sofa at home"></div>
<h1 class="abs hero-title head-font">More Happiness and<br>Satisfaction in Life</h1>
<p class="abs hero-text">Lorem ipsum dolor sit amet, consectetur adipi scing elit, sed do eiusmod tempor incidid unt ut labore et dolore magna aliqua.</p>
<div class="abs btn-orange hero-btn">READ MORE</div>

<!-- ABOUT -->
<div class="abs sky about"></div>
<svg class="abs" style="left:0;top:600px" width="1200" height="240" viewBox="0 0 1200 240">
  <path d="M0 185 C300 200 700 140 1200 20 V240 H0 Z" fill="#eef7fc"/>
  <path d="M0 190 C220 190 520 160 810 135 C560 175 260 205 0 232 Z" fill="#5ec72e"/>
</svg>
<div class="abs center" style="top:868px"><span class="eyebrow">WHO WE ARE</span></div>
<h2 class="abs center section-title head-font" style="top:904px">Fostering Mental Clarity</h2>
<p class="abs about-text">Lorem ipsum dolor sit amet, consectetur adipiscing elit, sed do eiusmod tempor incididunt ut labore et dolore magna aliqua . Ut enim ad minim veniam, quis laboris nisi ut aliquip ex ea commodo consequat. Lorem ipsum dolor sit am et, consectetur adipiscing elit, sed do eiusmod te a</p>

<div class="abs card" style="left:152px">
  <svg class="card-icon" width="52" height="56" viewBox="0 0 52 56" fill="none" stroke="#f6a320" stroke-width="3" stroke-linecap="round" stroke-linejoin="round">
    <path d="M4 50 H48"/><path d="M8 50 C8 40 16 32 26 30 L36 44"/><path d="M20 8 L30 24 L38 20 L28 4 Z"/>
  </svg>
  <div class="card-title head-font low">CLIENT-CENTRIC</div>
</div>
<div class="abs card" style="left:462px">
  <div class="card-title head-font card-pro-title">PROFESSIONAL</div>
  <p class="card-pro-text">Lorem ipsum dolor sit amet, consectetur adipiscing elit, se d do eiusmod tempor incidid unt ut labore et dolore magna ali</p>
  <svg class="abs" style="left:168px;top:150px" width="100" height="90" viewBox="0 0 100 90" fill="none" stroke="#f6c27a" stroke-width="5" opacity=".45">
    <circle cx="50" cy="55" r="45"/><path d="M50 25 V55 L65 65"/>
  </svg>
</div>
<div class="abs card" style="left:769px">
  <svg class="card-icon" width="56" height="56" viewBox="0 0 56 56" fill="none" stroke="#f6a320" stroke-width="3">
    <path d="M28 6 L50 22 L42 48 H14 L6 22 Z"/>
    <circle cx="28" cy="6" r="4" fill="#fff"/><circle cx="50" cy="22" r="4" fill="#fff"/><circle cx="42" cy="48" r="4" fill="#fff"/><circle cx="14" cy="48" r="4" fill="#fff"/><circle cx="6" cy="22" r="4" fill="#fff"/>
  </svg>
  <div class="card-title head-font low">EXPERTISE</div>
</div>

<!-- MINDS -->
<div class="abs minds-eyebrow"><span class="eyebrow" style="font-size:11px">WHO WE ARE</span></div>
<h2 class="abs minds-title head-font">Strengthening Minds,<br>Healing Hearts</h2>
<h3 class="abs minds-sub head-font">Helping You Find Inner Balance</h3>
<p class="abs minds-text" style="top:1718px">Lorem ipsum dolor sit amet, consectetur adipiscing elit, sed do eiusmod temp or incididunt ut labore et dolore magna aliqua. Ut enim ad minim veniam, quis laboris nisi ut aliquip ex ea commodo consequat.</p>
<p class="abs minds-text" style="top:1786px">Lorem ipsum dolor sit amet, consectetur adipiscing elit, sed do eiusmod temp or incididunt ut labore et dolore magna aliqua.</p>
<div class="abs btn-contact">Contact us
  <svg width="16" height="12" viewBox="0 0 16 12" fill="none" stroke="#fff" stroke-width="1.6"><path d="M1 6 H15 M10 1 L15 6 L10 11"/></svg>
</div>
<div class="abs circle" style="left:670px;top:1500px;width:400px;height:400px;background:#eef3dc"></div>
<div class="abs circle" style="left:651px;top:1813px;width:94px;height:94px;background:var(--green)"></div>
<div class="abs circle" role="img" aria-label="Portrait photo of a smiling senior man with glasses" style="left:642px;top:1492px;width:426px;height:426px;background:radial-gradient(circle at 55% 40%,#c9ccd2 0%,#9ea8b6 45%,#3f63a8 80%,#2f56a2 100%)"></div>
<div class="abs circle" role="img" aria-label="Photo of a therapist in conversation with a client" style="left:952px;top:1534px;width:200px;height:200px;background:linear-gradient(135deg,#d8dde2,#a4aeb5 60%,#7f8a7e)"></div>

<!-- SERVICES -->
<div class="abs" role="img" aria-label="Photo of a therapist taking notes on a clipboard" style="left:0;top:2058px;width:340px;height:452px;background:linear-gradient(135deg,#e9e7e4,#bdb6ad 55%,#8a8178)"></div>
<div class="abs svc-vertical" style="left:340px;top:2058px;width:60px;height:452px"></div>
<div class="abs vlabel" style="left:352px;top:2470px"><b>→ Emotion Regulation</b><small>Lorem ipsum dolor sit amet, consectetu</small></div>
<div class="abs" role="img" aria-label="Photo of a father and child smiling together" style="left:400px;top:2058px;width:400px;height:452px;background:linear-gradient(160deg,#cfc9c0,#9a8f84 55%,#5a5048)"></div>
<div class="abs svc-overlay"></div>
<div class="abs circle" style="left:439px;top:2311px;width:60px;height:60px;background:var(--white);display:flex;align-items:center;justify-content:center">
  <svg width="30" height="30" viewBox="0 0 30 30" fill="none" stroke="#1c3a53" stroke-width="2" stroke-linecap="round"><path d="M3 27 H27"/><path d="M6 27 C6 20 10 16 16 15 L21 24"/><path d="M11 4 L17 13 L21 11 L15 2 Z"/></svg>
</div>
<div class="abs svc-title">Ego State Therapy</div>
<p class="abs svc-text">Lorem ipsum dolor sit amet, consectetur adipiscing elit, sed do eiusmod tempor incididunt ut labore et dolore magna aliqua. Ut enim ad minim</p>
<svg class="abs" style="left:439px;top:2478px" width="26" height="14" viewBox="0 0 26 14" fill="none" stroke="#fff" stroke-width="1.6"><path d="M1 7 H25 M19 1 L25 7 L19 13"/></svg>
<div class="abs" role="img" aria-label="Photo of a young woman listening thoughtfully during a therapy session" style="left:800px;top:2058px;width:340px;height:452px;background:linear-gradient(135deg,#d9c6b3,#b98a6c 45%,#8a6a57)"></div>
<div class="abs svc-vertical" style="left:1140px;top:2058px;width:60px;height:452px"></div>
<div class="abs vlabel" style="left:1152px;top:2470px"><b>→ Imaginative Structure</b><small>Lorem ipsum dolor sit amet, consectetu</small></div>

<!-- TESTIMONIALS -->
<div class="abs sky testi"></div>
<div class="abs center testi-label">TESTIMONIALS</div>
<h2 class="abs center testi-title head-font">What Our Clients are Saying</h2>
<svg class="abs" style="left:0;top:2700px" width="1200" height="220" viewBox="0 0 1200 220" fill="none">
  <path d="M198 190 C260 120 330 80 382 74 C470 48 540 32 603 32 C666 32 736 48 824 74 C876 80 946 120 1009 190" stroke="#3a7fd6" stroke-width="2" stroke-dasharray="7 6"/>
</svg>
<div class="abs circle" role="img" aria-label="Client portrait" style="left:161px;top:2853px;width:74px;height:74px;background:#b9b2ab;border:3px solid #fff"></div>
<div class="abs circle" role="img" aria-label="Client portrait" style="left:345px;top:2737px;width:74px;height:74px;background:#a89e95;border:3px solid #fff"></div>
<div class="abs circle" role="img" aria-label="Featured client portrait" style="left:543px;top:2672px;width:120px;height:120px;background:#8e8179;border:4px solid #fff"></div>
<div class="abs circle" role="img" aria-label="Client portrait" style="left:787px;top:2737px;width:74px;height:74px;background:#c2b7a5;border:3px solid #fff"></div>
<div class="abs circle" role="img" aria-label="Client portrait" style="left:972px;top:2853px;width:74px;height:74px;background:#b0aca8;border:3px solid #fff"></div>
<svg class="abs" style="left:578px;top:2833px" width="46" height="36" viewBox="0 0 46 36" fill="#2f7de1">
  <path d="M0 36 V18 C0 8 6 2 16 0 L18 5 C12 7 10 11 10 16 H20 V36 Z"/>
  <path d="M26 36 V18 C26 8 32 2 42 0 L44 5 C38 7 36 11 36 16 H46 V36 Z"/>
</svg>
<p class="abs testi-text">Lorem ipsum dolor sit amet, consectetur adipiscing elit, sed do eiusmod te dunt ut labore et dolore magna aliqua .dipiscing elit, sed do eiusmod temp dunt ut labore et dolore magna aliqua .dipiscing elit, sed</p>
<div class="abs center stars">★★★★★</div>
<div class="abs center testi-name">Lukas Brenner</div>
<div class="abs center testi-role">Client</div>
<div class="abs arrow-btn" style="left:465px;top:3021px;background:var(--navy-deep)">
  <svg width="20" height="16" viewBox="0 0 20 16" fill="none" stroke="#fff" stroke-width="2"><path d="M19 8 H2 M8 2 L2 8 L8 14"/></svg>
</div>
<div class="abs arrow-btn" style="left:696px;top:3021px;background:var(--blue)">
  <svg width="20" height="16" viewBox="0 0 20 16" fill="none" stroke="#fff" stroke-width="2"><path d="M1 8 H18 M12 2 L18 8 L12 14"/></svg>
</div>

<!-- CONTACT -->
<h2 class="abs contact-title head-font"><b>Get &nbsp;in Touch</b><br>Contact Us</h2>
<p class="abs contact-text">Lorem ipsum dolor sit amet, consectetur adipiscing e lit, sed do eiusmod tempor incididunt ut labore et dolore magna aliqua. ceptos ...</p>
<div class="abs contact-rule"></div>
<div class="abs contact-row" style="top:3512px">
  <div class="contact-ico"><svg width="14" height="18" viewBox="0 0 14 18"><path d="M7 0 C3 0 0 3 0 7 C0 12 7 18 7 18 C7 18 14 12 14 7 C14 3 11 0 7 0 Z" fill="#f6a320"/><circle cx="7" cy="7" r="2.5" fill="#fff"/></svg></div>
  <span>Birkenweg 7, 4820 Talheim</span>
</div>
<div class="abs contact-row" style="top:3576px">
  <div class="contact-ico"><svg width="16" height="16" viewBox="0 0 16 16"><path d="M3 1 L6 1 L7 5 L5 6 C6 8 8 10 10 11 L11 9 L15 10 L15 13 C15 14 14 15 13 15 C6 15 1 10 1 3 C1 2 2 1 3 1 Z" fill="#f6a320"/></svg></div>
  <span>+43 1 5550 1234</span>
</div>
<div class="abs contact-row" style="top:3629px">
  <div class="contact-ico"><svg width="16" height="12" viewBox="0 0 16 12"><rect width="16" height="12" rx="1.5" fill="#f6a320"/><path d="M1 1 L8 7 L15 1" stroke="#fff" stroke-width="1.4" fill="none"/></svg></div>
  <span>praxis@stillewege.example</span>
</div>

<div class="abs form-card"></div>
<div class="abs f-label" style="left:624px;top:3266px">Full Name:</div>
<div class="abs f-input" style="left:620px;top:3298px;width:422px">Sed non neque elit.</div>
<div class="abs f-label" style="left:624px;top:3370px">Email :</div>
<div class="abs f-label" style="left:850px;top:3370px">Phone no :</div>
<div class="abs f-input" style="left:620px;top:3402px;width:196px">Sed non neque elit.</div>
<div class="abs f-input" style="left:846px;top:3402px;width:196px">Sed non neque elit.</div>
<div class="abs f-label" style="left:624px;top:3480px">Messages &nbsp;:</div>
<div class="abs f-input" style="left:620px;top:3511px;width:422px;height:128px">Sed non neque elit.</div>
<div class="abs submit">SUBMIT</div>

<!-- FOOTER -->
<svg class="abs" style="left:0;top:3800px" width="1200" height="520" viewBox="0 0 1200 520">
  <path d="M0 215 C260 130 560 100 900 92 C1030 88 1130 80 1200 70 V520 H0 Z" fill="#1c3a53"/>
  <path d="M390 108 C650 60 900 40 1200 5 V70 C1000 80 800 80 600 90 C520 94 450 100 390 108 Z" fill="#5ec72e"/>
</svg>
<div class="abs footer-h" style="left:94px;top:4060px">CONTACT US</div>
<div class="abs footer-small" style="left:94px;top:4100px;display:flex;gap:16px">
  <svg width="12" height="16" viewBox="0 0 14 18"><path d="M7 0 C3 0 0 3 0 7 C0 12 7 18 7 18 C7 18 14 12 14 7 C14 3 11 0 7 0 Z" fill="#fff"/><circle cx="7" cy="7" r="2.5" fill="#1c3a53"/></svg>
  <span>101- lorem ipsum simple text<br>print type text industry text.</span>
</div>
<div class="abs footer-small" style="left:94px;top:4160px;display:flex;gap:16px;align-items:center">
  <svg width="13" height="13" viewBox="0 0 16 16"><path d="M3 1 L6 1 L7 5 L5 6 C6 8 8 10 10 11 L11 9 L15 10 L15 13 C15 14 14 15 13 15 C6 15 1 10 1 3 C1 2 2 1 3 1 Z" fill="#fff"/></svg>
  <span>555 010 2030</span>
</div>
<div class="abs footer-small" style="left:94px;top:4196px;display:flex;gap:16px;align-items:center">
  <svg width="15" height="11" viewBox="0 0 16 12"><rect width="16" height="12" rx="1.5" fill="#fff"/><path d="M1 1 L8 7 L15 1" stroke="#1c3a53" stroke-width="1.4" fill="none"/></svg>
  <span>hallo@stillewege.example</span>
</div>

<div class="abs" style="left:380px;top:4002px;width:72px;height:72px;border:3px solid #fff"></div>
<div class="abs footer-brand">Stille Wege<br>&nbsp;&nbsp;&nbsp;...zur Gelassenheit</div>
<p class="abs footer-small" style="left:460px;top:4104px;width:290px;text-align:center">Lorem ipsum dolor sit amet, consectetur adipisc ing elit, sed do eiusmod tempor incididunt bbbbbut bccbbcbnmx zjzmsmmzm</p>
<div class="abs social" style="left:537px;top:4190px"></div>
<div class="abs social" style="left:581px;top:4190px"></div>
<div class="abs social" style="left:625px;top:4190px"></div>

<div class="abs footer-h" style="right:94px;top:4060px">OPENING HOURS</div>
<div class="abs hours" style="top:4104px"><span>Mon - Fri: 9am - to - 6pm</span><svg width="16" height="16" viewBox="0 0 16 16" fill="none" stroke="#fff" stroke-width="1.4"><circle cx="8" cy="8" r="7"/><path d="M8 4 V8 H11"/></svg></div>
<div class="abs hours" style="top:4135px"><span>Saturday 9am - to - 2pm</span><svg width="16" height="16" viewBox="0 0 16 16" fill="none" stroke="#fff" stroke-width="1.4"><circle cx="8" cy="8" r="7"/><path d="M8 4 V8 H11"/></svg></div>
<div class="abs hours" style="top:4166px"><span>Sunday : <u>Closed</u></span><svg width="16" height="16" viewBox="0 0 16 16" fill="none" stroke="#fff" stroke-width="1.4"><circle cx="8" cy="8" r="7"/><path d="M8 4 V8 H11"/></svg></div>

<div class="abs" style="left:62px;top:4270px;width:1076px;height:1px;background:#3d5a72"></div>
<div class="abs center footer-small" style="top:4282px">Stille Wege</div>

</body>
</html>
```